New stationary design for online film company

We need some new stationary to fit with our new logo. The stationary should be professional, clean and simple.
We need designs for a full set of business stationary.
We need - letterhead, envelopes, invoices, proposals, coverslip/note and cover page

Industry/Entity Type

Business

```html
<!DOCTYPE html>
<html lang="en">
<head>
<meta charset="utf-8">
<title>Lumoreel Stationery Set</title>
<link href="https://fonts.googleapis.com/css2?family=Montserrat:wght@600&family=Open+Sans:wght@400;600&display=swap" rel="stylesheet">
<style>
  :root {
    --navy: #0f4a75;
    --sky: #6a9bb8;
    --paper: #ffffff;
    --paper-shade: #eef0f3;
    --ink: #4a4f55;
    --ghost: #e3e6ee;
    --backdrop: #d9dadc;
    --label: #ffffff;
    --label-bg: #8c9096;
  }
  * { box-sizing: border-box; margin: 0; padding: 0; }
  html, body { width: 1200px; height: 486px; overflow: hidden; }
  body {
    position: relative;
    background: var(--backdrop);
    font-family: "Open Sans", Arial, sans-serif;
    color: var(--ink);
  }
  .sheet {
    position: absolute;
    background: linear-gradient(160deg, var(--paper) 55%, var(--paper-shade));
    box-shadow: 0 2px 6px rgba(0,0,0,.18);
    overflow: hidden;
  }
  .brand {
    position: absolute;
    display: flex;
    align-items: center;
    gap: 5px;
    font-family: "Montserrat", Arial, sans-serif;
    font-weight: 600;
    color: var(--navy);
    line-height: 1;
    white-space: nowrap;
  }
  .brand-dot { border-radius: 50%; background: var(--navy); flex: none; }

  .letterhead { top: 18px; width: 332px; height: 430px; }
  .letterhead--one { left: 8px; }
  .letterhead--two { left: 373px; }
  .letterhead .brand { top: 26px; font-size: 23px; }
  .letterhead .brand-dot { width: 20px; height: 20px; }
  .letterhead--one .brand { left: 50%; transform: translateX(-50%); }
  .letterhead--two .brand { left: 13px; }

  .watermark-circle {
    position: absolute;
    left: 96px; top: 170px;
    width: 146px; height: 146px;
    border-radius: 50%;
    background: var(--ghost);
  }
  .footer-line {
    position: absolute;
    left: 0; right: 0; bottom: 9px;
    display: flex; justify-content: center; gap: 10px;
    font-size: 5.4px;
  }
  .footer-line span + span { border-left: 1px solid #aab; padding-left: 6px; }

  .contact-block {
    position: absolute;
    left: 257px; top: 19px;
    border-left: 1px solid #c9ced4;
    padding-left: 4px;
    font-size: 5.4px;
    line-height: 1.55;
  }
  .contact-block .gap { height: 4px; }

  .url-band { position: absolute; left: 0; bottom: 0; width: 100%; }
  .url-band text { font-family: "Open Sans", Arial, sans-serif; font-size: 5.6px; letter-spacing: 1.2px; fill: var(--paper); }

  .envelope-back, .envelope-open { position: absolute; box-shadow: 0 2px 6px rgba(0,0,0,.18); background: var(--paper); }
  .envelope-back { left: 818px; top: 4px; width: 371px; height: 236px; }
  .envelope-open { left: 738px; top: 76px; width: 371px; height: 166px; }
  .flap-mark { position: absolute; border-radius: 50%; }
  .envelope-back .flap-mark { left: 169px; top: 22px; width: 32px; height: 32px; background: var(--paper); }
  .envelope-open .flap-mark { left: 169px; top: 35px; width: 30px; height: 30px; background: var(--navy); }

  .envelope-front { left: 778px; top: 150px; width: 372px; height: 166px; }
  .envelope-front .brand { left: 10px; top: 21px; font-size: 20px; }
  .envelope-front .brand-dot { width: 17px; height: 17px; }
  .envelope-front .address { position: absolute; left: 35px; top: 45px; font-size: 5.4px; }

  .card { top: 344px; width: 185px; height: 105px; }
  .card--front { left: 770px; }
  .card--back { left: 971px; }
  .card--front .brand { left: 8px; top: 42px; font-size: 15px; }
  .card--front .brand-dot { width: 13px; height: 13px; }
  .card-details {
    position: absolute; left: 118px; top: 27px;
    border-left: 1px solid #c9ced4; padding-left: 4px;
    font-size: 4.6px; line-height: 1.55;
  }
  .card-details .name { font-weight: 600; color: var(--navy); font-size: 6.4px; line-height: 1.1; }
  .card-details .title { color: var(--sky); margin-bottom: 3px; }
  .card--front .address { position: absolute; left: 7px; bottom: 8px; font-size: 4.6px; }
  .card--back .brand { left: 50%; top: 36px; transform: translateX(-50%); font-size: 18px; }
  .card--back .brand-dot { width: 15px; height: 15px; }
  .card--back .web { position: absolute; left: 0; right: 0; top: 92px; text-align: center; font-size: 6px; letter-spacing: 1.4px; }

  .option-label {
    position: absolute; top: 458px;
    font-size: 22px; color: var(--label);
    background: var(--label-bg); padding: 0 8px; border-radius: 3px; line-height: 26px;
  }
  .option-label--one { left: 117px; }
  .option-label--two { left: 481px; }
</style>
</head>
<body>

  <section class="sheet letterhead letterhead--one">
    <div class="brand"><span class="brand-dot"></span>lumoreel</div>
    <div class="watermark-circle"></div>
    <div class="footer-line">
      <span>Street Name, City Name, State Zip Code</span>
      <span>&#9742; 123-456-0789</span>
      <span>&#9993; info@lumoreel.com</span>
      <span>www.lumoreel.com</span>
    </div>
  </section>

  <section class="sheet letterhead letterhead--two">
    <div class="brand"><span class="brand-dot"></span>lumoreel</div>
    <div class="contact-block">
      <div>&#9742; 123-456-0789</div>
      <div>&#9993; info@lumoreel.com</div>
      <div class="gap"></div>
      <div>Street Name, City Name</div>
      <div>State Zip Code</div>
    </div>
    <svg class="url-band" viewBox="0 0 332 12" width="332" height="12">
      <rect x="0" y="5" width="332" height="2" fill="var(--sky)"/>
      <path d="M0 9 H222 Q228 9 230 3 Q232 0 238 0 H332 V12 H0 Z" fill="var(--navy)"/>
      <text x="250" y="8.5">www.lumoreel.com</text>
    </svg>
  </section>

  <section class="envelope-back">
    <svg width="371" height="236" viewBox="0 0 371 236" style="position:absolute;left:0;top:0">
      <path d="M0 0 H371 V20 Q350 30 290 50 L215 70 Q185 78 156 70 L80 50 Q20 30 0 20 Z" fill="var(--navy)"/>
    </svg>
    <div class="flap-mark"></div>
  </section>

  <section class="envelope-open">
    <svg width="371" height="166" viewBox="0 0 371 166" style="position:absolute;left:0;top:0">
      <path d="M1 1 H370 V12 Q350 30 290 52 L215 74 Q185 82 156 74 L80 52 Q20 30 1 12 Z" fill="none" stroke="#222" stroke-width="0.8"/>
    </svg>
    <div class="flap-mark"></div>
  </section>

  <section class="sheet envelope-front">
    <div class="brand"><span class="brand-dot"></span>lumoreel</div>
    <div class="address">Street Name, City Name, State Zip Code</div>
    <svg class="url-band" viewBox="0 0 372 12" width="372" height="12">
      <rect x="0" y="5" width="372" height="2" fill="var(--sky)"/>
      <path d="M0 9 H252 Q258 9 260 3 Q262 0 268 0 H372 V12 H0 Z" fill="var(--navy)"/>
      <text x="282" y="8.5">www.lumoreel.com</text>
    </svg>
  </section>

  <section class="sheet card card--front">
    <div class="brand"><span class="brand-dot"></span>lumoreel</div>
    <div class="card-details">
      <div class="name">Your Name</div>
      <div class="title">Title</div>
      <div>&#9742; 123-456-0789</div>
      <div>&#9743; 123-456-0789</div>
      <div>&#9993; info@lumoreel.com</div>
    </div>
    <div class="address">Street Name, City Name, State Zip Code</div>
    <svg class="url-band" viewBox="0 0 185 10" width="185" height="10">
      <rect x="0" y="4" width="185" height="1.6" fill="var(--sky)"/>
      <path d="M0 7 H112 Q117 7 119 2.5 Q121 0 126 0 H185 V10 H0 Z" fill="var(--navy)"/>
      <text x="131" y="7" style="font-size:4.8px;letter-spacing:0.9px">www.lumoreel.com</text>
    </svg>
  </section>

  <section class="sheet card card--back">
    <div class="brand"><span class="brand-dot"></span>lumoreel</div>
    <div class="web">www.lumoreel.com</div>
  </section>

  <div class="option-label option-label--one">Option-1</div>
  <div class="option-label option-label--two">Option-2</div>

</body>
</html>
```